Book Cover "Venice"

Creation of a cover (14 x 20.5 cm + bleed area) for a book:
Image: “BrumeVerte” (Tiff joined)
AUTHOR: Corinne Valmer
TITLE: The murmurs of Lorient
PUBLISHER: Editions Pluvane (AT THE BOTTOM OF THE COVER)

Target Market(s)

Readers of romantic novels

Industry/Entity Type

Book

```html
<!DOCTYPE html>
<html lang="en">
<head>
<meta charset="utf-8">
<title>The murmurs of Lorient — Book Cover</title>
<link rel="stylesheet" href="https://fonts.googleapis.com/css2?family=Cormorant+Garamond:wght@400;500&family=Playball&display=swap">
<style>
  :root {
    --page-bg: #dfe5ea;
    --ink-light: #ffffff;
    --sky-top: #3c0a12;
    --sky-upper: #a3141b;
    --sky-mid: #e0281d;
    --sky-glow: #f23a1c;
    --sky-low: #c41f17;
    --skyline-dark: #1a0708;
  }
  * { margin: 0; padding: 0; box-sizing: border-box; }
  html, body {
    width: 1200px;
    height: 1123px;
    overflow: hidden;
    background: var(--page-bg);
  }
  .canvas {
    position: relative;
    width: 1200px;
    height: 1123px;
  }
  .cover {
    position: absolute;
    left: 237px;
    top: 30px;
    width: 726px;
    height: 1063px;
    overflow: hidden;
    color: var(--ink-light);
    text-align: center;
  }
  .cover-art {
    position: absolute;
    inset: 0;
    background: linear-gradient(
      to bottom,
      var(--sky-top) 0%,
      var(--sky-upper) 16%,
      var(--sky-mid) 38%,
      var(--sky-glow) 60%,
      var(--sky-low) 76%,
      var(--skyline-dark) 100%
    );
  }
  .author-label,
  .publisher-label {
    position: absolute;
    left: 0;
    right: 0;
    font-family: "Cormorant Garamond", Georgia, serif;
    font-weight: 500;
    letter-spacing: 0.04em;
    text-transform: uppercase;
  }
  .author-label { top: 114px; font-size: 23px; }
  .author-name {
    position: absolute;
    left: 0;
    right: 0;
    top: 148px;
    font-family: "Cormorant Garamond", Georgia, serif;
    font-weight: 500;
    font-size: 47px;
    letter-spacing: 0.04em;
  }
  .title {
    position: absolute;
    left: 0;
    right: 0;
    top: 290px;
    font-family: "Playball", cursive;
    font-weight: 400;
    font-size: 112px;
    line-height: 132px;
  }
  .title span { display: block; }
  .publisher-label { top: 952px; font-size: 19px; }
  .publisher-name {
    position: absolute;
    left: 0;
    right: 0;
    top: 980px;
    font-family: "Cormorant Garamond", Georgia, serif;
    font-weight: 500;
    font-size: 33px;
    letter-spacing: 0.02em;
  }
</style>
</head>
<body>
  <main class="canvas">
    <section class="cover">
      <div class="cover-art" role="img" aria-label="Photograph: blazing red sunset sky over a harbour town skyline of domes and bell towers in silhouette, with glowing street lanterns in the foreground"></div>
      <p class="author-label">Author</p>
      <p class="author-name">Corinne Valmer</p>
      <h1 class="title"><span>The murmurs</span><span>of Lorient</span></h1>
      <p class="publisher-label">Publisher</p>
      <p class="publisher-name">Editions Pluvane</p>
    </section>
  </main>
</body>
</html>
```